FinTech company looking to revamp and expand client-facing interface for our financial models

Halvern Ledgerworks currently has a very simple website that allows clients to interact with our financial models. We are looking to completely redesign the current site and add several extra pages to provide extra functionality. We want the design to have a modern, slick feel, that will work on both a desktop or a tablet. It should be straightforward for clients to move between different pages at any time, and clear from the layout how to interact with the more advanced features. We have included screenshots of existing pages in the attached design brief, as well as sketches of the functionality required by the new pages, but can't provide a direct link to the current site.
Target Market(s)
Professional investors that will be paying to access the interface
Industry/Entity Type
Finance
Number of Pages Required
4 page
Colors
Designer to choose colors to be used in the design.
Look and feel
Each slider illustrates characteristics of the customer's brand and the style your logo design should communicate.

```html
<!DOCTYPE html>
<html lang="en">
<head>
<meta charset="utf-8">
<title>QVERO – Models</title>
<link rel="stylesheet" href="https://fonts.googleapis.com/css2?family=Roboto:wght@300;400;500&display=swap">
<style>
:root{
  --bar:#43423d;
  --bar-active:#353430;
  --blue:#0b5cb4;
  --row-light:#efeef0;
  --row-dark:#dddcde;
  --grid:#ffffff;
  --ink:#222;
  --muted:#555;
  --white:#fff;
}
*{box-sizing:border-box;margin:0;padding:0}
html,body{width:1200px;height:743px;overflow:hidden}
body{position:relative;background:#fff;font-family:'Roboto',Arial,sans-serif;color:var(--ink)}
.topbar{position:absolute;left:0;top:0;width:1200px;height:70px;background:var(--bar);color:var(--white)}
.brand{position:absolute;left:197px;top:20px;font-size:23px;font-weight:400;letter-spacing:.5px}
.tabs{position:absolute;left:318px;top:0;display:flex;height:70px}
.tab{width:60px;display:flex;align-items:center;justify-content:center;font-size:13px;font-weight:500;padding-top:2px}
.tab.active{background:var(--bar-active)}
.mainnav{position:absolute;right:176px;top:0;height:70px;display:flex;align-items:center;gap:22px;font-size:13px;font-weight:500}
.mainnav span{display:flex;align-items:center;gap:4px}
.mainnav svg{width:12px;height:12px;fill:#fff}
.filter-label{position:absolute;left:172px;top:124px;font-size:13px;color:var(--ink)}
.filter-box{position:absolute;left:172px;top:148px;width:405px;height:53px;border:1px solid #888;font-size:13px}
.filter-box .all{position:absolute;left:19px;top:19px}
.radio{position:absolute;left:53px;top:20px;width:12px;height:12px;border:1px solid #888;border-radius:50%;background:#fff}
.radio::after{content:"";position:absolute;left:2px;top:2px;width:6px;height:6px;border-radius:50%;background:#777}
.filter-box .thr{position:absolute;left:82px;top:19px}
.slider{position:absolute;left:165px;top:20px;width:142px;height:12px}
.slider-label{position:absolute;top:34px;font-size:12px}
.chev{position:absolute;left:381px;top:21px;width:10px;height:8px}
.export{position:absolute;left:172px;top:244px;font-size:12px;display:flex;align-items:center;gap:5px}
.export svg{width:11px;height:11px}
.hscroll{position:absolute;left:456px;top:248px;width:571px;height:15px;border:1px solid #ccc;background:#fff}
.hscroll .arrow{position:absolute;top:-1px;width:18px;height:15px;background:#5c5b57;display:flex;align-items:center;justify-content:center}
.hscroll .arrow.left{left:-1px}.hscroll .arrow.right{right:-1px}
.hscroll .thumb{position:absolute;left:32px;top:2px;width:184px;height:9px;border-radius:5px;background:#666}
.data-table{position:absolute;left:172px;top:273px;border-collapse:collapse;table-layout:fixed;width:855px;box-shadow:0 6px 10px rgba(0,0,0,.25)}
.data-table th{background:var(--blue);color:#fff;font-size:13px;font-weight:400;height:48px;border-right:1px solid rgba(255,255,255,.45)}
.data-table td{font-size:11px;text-align:center;height:49px;border-right:1px solid var(--grid);border-bottom:1px solid #c9c8ca;line-height:14px}
.data-table tr:nth-child(odd) td{background:var(--row-light)}
.data-table tr:nth-child(even) td{background:var(--row-dark)}
.data-table tr:last-child td{height:47px;border-bottom:none}
.sort{display:inline-block;margin-left:6px;vertical-align:middle;width:0;height:0;border-left:4px solid transparent;border-right:4px solid transparent;border-top:5px solid #fff}
.add-column{position:absolute;left:1028px;top:273px;width:60px;height:48px;background:var(--bar);color:#fff;font-size:12px;text-align:center;line-height:14px;padding-top:11px;box-shadow:0 4px 8px rgba(0,0,0,.3)}
.add-column svg{position:absolute;right:3px;top:3px;width:12px;height:12px}
.fav-btn{position:absolute;left:866px;top:585px;width:161px;height:44px;background:var(--bar);color:#fff;font-size:14px;display:flex;align-items:center;justify-content:center;gap:7px}
.fav-btn svg{width:12px;height:12px}
.footer{position:absolute;left:0;top:682px;width:1200px;height:61px;background:var(--bar);color:#fff;font-size:12px;text-align:center;line-height:61px}
</style>
</head>
<body>
<header class="topbar">
  <div class="brand">QVERO</div>
  <nav class="tabs">
    <div class="tab active">250D</div>
    <div class="tab">83D</div>
    <div class="tab">42D</div>
  </nav>
  <nav class="mainnav">
    <span><svg viewBox="0 0 12 12"><path d="M6 1 0 6.5h1.6V11h3.2V8h2.4v3h3.2V6.5H12z"/></svg>MODELS</span>
    <span><svg viewBox="0 0 12 12"><path d="M5 0h2l.3 1.6 1.2.5 1.4-1 1.4 1.4-1 1.4.5 1.2L12 5v2l-1.6.3-.5 1.2 1 1.4-1.4 1.4-1.4-1-1.2.5L7 12H5l-.3-1.6-1.2-.5-1.4 1-1.4-1.4 1-1.4-.5-1.2L0 7V5l1.6-.3.5-1.2-1-1.4 1.4-1.4 1.4 1 1.2-.5zM6 4a2 2 0 1 0 0 4 2 2 0 0 0 0-4z"/></svg>SENSITIVITIES</span>
    <span><svg viewBox="0 0 12 12"><path d="M6 0l1.8 3.9 4.2.4-3.2 2.8 1 4.1L6 9.1 2.2 11.2l1-4.1L0 4.3l4.2-.4z"/></svg>FAVOURITES</span>
  </nav>
</header>

<div class="filter-label">Filter</div>
<div class="filter-box">
  <span class="all">ALL</span>
  <span class="radio"></span>
  <span class="thr">THRESHOLD</span>
  <svg class="slider" viewBox="0 0 142 12"><path d="M1 0v12M141 0v12M1 6h140" stroke="#333" stroke-width="2" fill="none"/></svg>
  <span class="slider-label" style="left:162px">0</span>
  <span class="slider-label" style="left:294px">100</span>
  <svg class="chev" viewBox="0 0 10 8"><path d="M1 2l4 4 4-4" stroke="#333" stroke-width="1.5" fill="none"/></svg>
</div>

<div class="export"><svg viewBox="0 0 11 11"><path d="M5.5 0v6M2.5 3.5l3 3 3-3" stroke="#222" stroke-width="2" fill="none"/><path d="M0 9h11v2H0z" fill="#222"/></svg>Export</div>

<div class="hscroll">
  <div class="arrow left"><svg width="6" height="8" viewBox="0 0 6 8"><path d="M5 0 1 4l4 4" stroke="#fff" fill="none"/></svg></div>
  <div class="thumb"></div>
  <div class="arrow right"><svg width="6" height="8" viewBox="0 0 6 8"><path d="M1 0l4 4-4 4" stroke="#fff" fill="none"/></svg></div>
</div>

<table class="data-table">
  <colgroup>
    <col style="width:71px"><col style="width:72px"><col style="width:70px"><col style="width:72px">
    <col style="width:71px"><col style="width:71px"><col style="width:71px"><col style="width:71px">
    <col style="width:71px"><col style="width:72px"><col style="width:71px"><col style="width:72px">
  </colgroup>
  <thead>
    <tr><th>ID<span class="sort"></span></th><th>SECTOR</th><th>TIME</th><th>QUALITY</th><th>STAT1</th><th>STAT2</th><th>STAT3</th><th>STAT4</th><th>STAT5</th><th>STAT6</th><th>STAT7</th><th>STAT8</th></tr>
  </thead>
  <tbody>
    <tr><td>Model 1</td><td>Materials</td><td>2019-07-03<br>12:15:00.000</td><td>30.2288</td><td>2.01574</td><td>23.305</td><td>-0.149368</td><td>22.3054</td><td>4.63714</td><td>0.945706</td><td>2.81949</td><td>2.60858</td></tr>
    <tr><td>Model 2</td><td>Industrials</td><td>2019-07-03<br>12:15:00.000</td><td>32.8694</td><td>0.87307</td><td>32.185</td><td>-0.0336927</td><td>33.9911</td><td>11.5693</td><td>-0.472968</td><td>-0.830458</td><td>6.80646</td></tr>
    <tr><td>Model 3</td><td>Consumer<br>Discretionary</td><td>2019-07-03<br>12:15:00.000</td><td>1.66002</td><td>-0.569222</td><td>159.814</td><td>0.0252328</td><td>172.616</td><td>10.2875</td><td>-0.750396</td><td>-0.385309</td><td>4.69146</td></tr>
    <tr><td>Model 4</td><td>Information<br>Technology</td><td>2019-07-03<br>12:15:00.000</td><td>45.6856</td><td>0.412148</td><td>202.488</td><td>0.00849232</td><td>205.834</td><td>11.9094</td><td>-0.137913</td><td>-0.449595</td><td>3.85106</td></tr>
    <tr><td>Model 5</td><td>Information<br>Technology</td><td>2019-07-03<br>12:15:00.000</td><td>75.7733</td><td>7.06728</td><td>188.605</td><td>0.016913</td><td>181.665</td><td>3.82241</td><td>0.981019</td><td>1.29847</td><td>3.34927</td></tr>
  </tbody>
</table>

<div class="add-column">ADD<br>COLUMN<svg viewBox="0 0 12 12"><circle cx="6" cy="6" r="6" fill="#fff"/><path d="M6 3v6M3 6h6" stroke="#43423d" stroke-width="1.6"/></svg></div>

<div class="fav-btn"><svg viewBox="0 0 12 12"><circle cx="6" cy="6" r="6" fill="#fff"/><path d="M6 3v6M3 6h6" stroke="#43423d" stroke-width="1.6"/></svg>Add to Favourites</div>

<footer class="footer">©Copyright information here</footer>
</body>
</html>
```